Package for Utensil Kit

we want to have a new design for our utensil kit, its a paper bag with both sides like files below. our website is www.peckbox.com and please use #FF6C0E as the main color and feel free to unleash your creativity.
the deadcut of the package is 14x26cm.pdf also showed the size.
in the front we want to show our band
in the back we need info list here:
1. www.peckbox.com and QR code
2.our locations (Now four) and phone number
3.other information needed

```html
<!DOCTYPE html>
<html lang="en">
<head>
<meta charset="utf-8">
<title>Peckbox Utensil Kit – Front</title>
<link rel="stylesheet" href="https://fonts.googleapis.com/css2?family=Archivo:wght@800&display=swap">
<style>
  :root {
    --brand-orange: #ec6a22;
    --seal-orange: #e36420;
    --seal-edge: #d25a1a;
    --ink: #262422;
    --label-cream: #f6f0ea;
    --art-light: #f4f4f4;
    --art-shade: #dadada;
    --page: #ffffff;
  }
  * { margin: 0; padding: 0; box-sizing: border-box; }
  html, body {
    width: 812px;
    height: 1200px;
    overflow: hidden;
    background: var(--page);
  }
  .canvas {
    position: relative;
    width: 812px;
    height: 1200px;
  }
  .pouch {
    position: absolute;
    left: 284px;
    top: 68px;
    width: 244px;
    height: 1066px;
    display: block;
  }
  .pouch-body { fill: var(--brand-orange); }
  .seal-strip { fill: var(--seal-orange); }
  .seal-line { stroke: var(--seal-edge); stroke-width: 1; opacity: 0.6; }
  .brand-name {
    font-family: "Archivo", Arial, sans-serif;
    font-weight: 800;
    font-size: 128px;
    fill: var(--ink);
  }
  .dish-name {
    font-family: "Archivo", Arial, sans-serif;
    font-weight: 800;
    font-size: 28px;
    fill: var(--ink);
  }
  .product-label {
    font-family: "Archivo", Arial, sans-serif;
    font-weight: 800;
    font-size: 24px;
    fill: var(--label-cream);
  }
</style>
</head>
<body>
<main class="canvas">
  <svg class="pouch" viewBox="0 0 244 1066" xmlns="http://www.w3.org/2000/svg" aria-label="Peckbox utensil kit pouch, front">
    <defs>
      <linearGradient id="artTone" x1="0" y1="0" x2="1" y2="1">
        <stop offset="0" stop-color="var(--art-light)"/>
        <stop offset="1" stop-color="var(--art-shade)"/>
      </linearGradient>
    </defs>

    <rect class="pouch-body" x="0" y="0" width="244" height="1066"/>
    <rect class="seal-strip" x="0" y="0" width="244" height="35"/>
    <rect class="seal-strip" x="0" y="1031" width="244" height="35"/>
    <line class="seal-line" x1="0" y1="35" x2="244" y2="35"/>
    <line class="seal-line" x1="0" y1="1031" x2="244" y2="1031"/>

    <path class="art-area-top" role="img" aria-label="Area for a white chicken illustration entering from the top right"
          fill="url(#artTone)"
          d="M60 110 L244 40 L244 300 Z"/>

    <path class="art-area-bottom" role="img" aria-label="Area for a white chicken illustration rising from the bottom left"
          fill="url(#artTone)"
          d="M0 840 L200 880 L0 1031 Z"/>

    <text class="brand-name" transform="translate(150 753) rotate(-90)" textLength="495" lengthAdjust="spacingAndGlyphs">Peckbox</text>
    <text class="dish-name" transform="translate(186 753) rotate(-90)" textLength="258" lengthAdjust="spacingAndGlyphs">HAINAN CHICKEN</text>

    <text class="product-label" x="122" y="790" text-anchor="middle" textLength="140" lengthAdjust="spacingAndGlyphs">UTENSIL KIT</text>
  </svg>
</main>
</body>
</html>
```